Business Card Design Project

Looking for a simple and stylish business card. We are an Advertising Company. The card Must feature the company logo (attached) and also this info.
p: 0481629054
e: sales@rv-promo.com.au
w: www.rv-promo.com.au
We Advertise mainly using TV screens featured in restaurants and cafe. See website for more about the business.
Not really looking for a plain background, but at the same time do not want to much happening in the Background. I am not really to fussy though with the design or the colour scheme, and I am leaving the creativity part up to you creative designers.

```html
<!DOCTYPE html>
<html lang="en">
<head>
<meta charset="utf-8">
<title>RV Promo – Business Card</title>
<link rel="stylesheet" href="https://fonts.googleapis.com/css2?family=Varela+Round&family=Open+Sans:ital,wght@1,400&display=swap">
<style>
  :root {
    --backdrop: #ebe6df;
    --brand-pink: #e31d5c;
    --brand-blue: #1a4b98;
    --card-white: #ffffff;
    --text-light: #ffffff;
  }
  * { margin: 0; padding: 0; box-sizing: border-box; }
  html, body {
    width: 1200px;
    height: 900px;
    overflow: hidden;
    background: var(--backdrop);
  }
  .business-card {
    position: absolute;
    left: 238px;
    top: 243px;
    width: 724px;
    height: 414px;
    background: var(--card-white);
  }
  .card-header {
    position: absolute;
    left: 0;
    top: 0;
    width: 100%;
    height: 231px;
    background: var(--brand-pink);
  }
  .divider-band {
    position: absolute;
    left: 0;
    top: 231px;
    width: 100%;
    height: 14px;
    background: var(--brand-blue);
  }
  .contact-list {
    position: absolute;
    left: 30px;
    top: 36px;
    list-style: none;
    font-family: "Varela Round", sans-serif;
    font-size: 26px;
    line-height: 34px;
    color: var(--text-light);
    transform: rotate(-5deg);
    transform-origin: left top;
  }
  .contact-list li:nth-child(2) { padding-left: 6px; }
  .contact-list li:nth-child(3) { padding-left: 12px; }
  .person {
    position: absolute;
    left: 439px;
    top: 142px;
    font-family: "Open Sans", sans-serif;
    font-style: italic;
    font-size: 30px;
    line-height: 40px;
    color: var(--text-light);
  }
  .brand-name {
    position: absolute;
    right: 22px;
    top: 268px;
    font-family: "Varela Round", sans-serif;
    font-size: 98px;
    line-height: 120px;
    letter-spacing: 2px;
    color: var(--brand-blue);
    white-space: nowrap;
  }
</style>
</head>
<body>
  <article class="business-card">
    <section class="card-header">
      <ul class="contact-list">
        <li class="contact-phone">0481629054</li>
        <li class="contact-email">sales@rv-promo.com.au</li>
        <li class="contact-web">www.rv-promo.com.au</li>
      </ul>
      <div class="person">
        <p class="person-role">Managing Director</p>
        <p class="person-name">Mark Delaren</p>
      </div>
    </section>
    <div class="divider-band"></div>
    <p class="brand-name">RV PROMO</p>
  </article>
</body>
</html>
```